Family portrait and Wedding photographer needs a flyer to promote buisness

Looking for a design for a flyer that is elegant and sophisticated that can show romance in wedding photography or art in family portraits. I like Vintage, warm colours. Flyer to include website www.mirelkastingphotography.com.au
and facebook link. for the time being just put anything, To include phrase. " Let me capture the moment so you can keep it forever" .
Wedding , Portrait & Real Estate Photography

Industry/Entity Type

Wedding

```html
<!DOCTYPE html>
<html lang="en">
<head>
<meta charset="utf-8">
<title>Mirel Kasting Photography – Flyer</title>
<link href="https://fonts.googleapis.com/css2?family=Amatic+SC:wght@700&family=Quicksand:wght@400;500&display=swap" rel="stylesheet">
<style>
  :root {
    --page-bg: #ffffff;
    --card-line: #8a8a8a;
    --panel: #ad9e92;
    --panel-shadow: rgba(60, 45, 35, 0.35);
    --photo-dark: #5a5438;
    --photo-wood: #a56f45;
    --photo-warm: #c08c5e;
    --text-light: #f6f1ec;
    --ornament: #4a3c36;
    --ornament-soft: rgba(74, 60, 54, 0.18);
    --web-text: #a08d7e;
  }
  html, body {
    margin: 0;
    padding: 0;
    width: 1200px;
    height: 1000px;
    overflow: hidden;
    background: var(--page-bg);
  }
  .canvas {
    position: relative;
    width: 1200px;
    height: 1000px;
  }
  .flyer {
    position: absolute;
    left: 354px;
    top: 131px;
    width: 522px;
    height: 735px;
    border: 1px solid var(--card-line);
    background: var(--page-bg);
  }
  .panel {
    position: absolute;
    left: 11px;
    top: 11px;
    width: 502px;
    height: 677px;
    background: var(--panel);
    box-shadow: 0 2px 6px var(--panel-shadow);
    overflow: hidden;
  }
  .hero-photo {
    position: absolute;
    left: 0;
    top: 0;
    width: 502px;
    height: 380px;
    background:
      radial-gradient(ellipse 55% 35% at 50% 72%, var(--photo-warm) 0%, rgba(192,140,94,0) 75%),
      linear-gradient(to bottom, var(--photo-dark) 0%, #6c5f42 28%, #8d6745 45%, var(--photo-wood) 62%, #a07a5c 82%, var(--panel) 100%);
    -webkit-mask-image:
      linear-gradient(to bottom, #000 72%, transparent 100%),
      linear-gradient(to right, transparent 0%, #000 6%, #000 94%, transparent 100%);
    -webkit-mask-composite: source-in;
            mask-image:
      linear-gradient(to bottom, #000 72%, transparent 100%),
      linear-gradient(to right, transparent 0%, #000 6%, #000 94%, transparent 100%);
            mask-composite: intersect;
  }
  .quote-frame {
    position: absolute;
    left: 100px;
    top: 364px;
    width: 312px;
    height: 202px;
  }
  .tagline {
    position: absolute;
    left: 0;
    top: 428px;
    width: 502px;
    margin: 0;
    text-align: center;
    font-family: "Amatic SC", cursive;
    font-weight: 700;
    font-size: 21px;
    line-height: 36px;
    text-transform: uppercase;
    color: var(--text-light);
  }
  .services {
    position: absolute;
    left: 0;
    top: 608px;
    width: 502px;
    margin: 0;
    text-align: center;
    font-family: "Quicksand", sans-serif;
    font-weight: 400;
    font-size: 18.3px;
    color: var(--text-light);
  }
  .photographer-name {
    position: absolute;
    left: 0;
    top: 651px;
    width: 502px;
    margin: 0;
    text-align: center;
    font-family: "Quicksand", sans-serif;
    font-weight: 400;
    font-size: 17.5px;
    color: var(--text-light);
  }
  .website {
    position: absolute;
    left: 0;
    top: 702px;
    width: 522px;
    margin: 0;
    text-align: center;
    font-family: "Quicksand", sans-serif;
    font-weight: 400;
    font-size: 18.5px;
    color: var(--web-text);
  }
</style>
</head>
<body>
  <main class="canvas">
    <article class="flyer">
      <section class="panel">
        <div class="hero-photo" role="img" aria-label="Photograph of a toddler in a party hat sitting on a wooden boardwalk beside a large blue-iced cupcake, with blue and white bunting strung overhead"></div>
        <svg class="quote-frame" viewBox="0 0 312 202" role="img" aria-label="Decorative vintage scroll frame around the tagline">
          <rect x="14" y="24" width="284" height="154" rx="60" ry="60" fill="var(--ornament-soft)" stroke="var(--ornament)" stroke-width="3"/>
          <rect x="28" y="38" width="256" height="126" rx="48" ry="48" fill="none" stroke="var(--ornament)" stroke-width="1.5"/>
        </svg>
        <p class="tagline">Let me capture the moment<br>so you can keep it forever</p>
        <p class="services">Wedding, Portrait &amp; Real Estate Photography</p>
        <p class="photographer-name">Mirel Kasting</p>
      </section>
      <p class="website">www.mirelkastingphotography.com.au</p>
    </article>
  </main>
</body>
</html>
```